Hoofcare business card

I would like to create a business card design for my hoofcare business.

Front Side- would like to just include the logo and text as per the uploaded files- text font to match logo (upper and lower case).

Back side
- Include the details and contact information provided on the uploaded file.
- Also included on the back side- the uploaded TRIVN logo- keep it small on a top or bottom corner
- for rovendix and Plumtawyo contacts- please use the logos next to my usernames

```html
<!DOCTYPE html>
<html lang="en">
<head>
<meta charset="utf-8">
<title>Ashvale Equine Hoofcare — Business Card</title>
<link href="https://fonts.googleapis.com/css2?family=Cinzel:wght@400;600&family=Cormorant+Garamond:wght@500&display=swap" rel="stylesheet">
<style>
  :root {
    --backdrop: #2b2b2e;
    --card: #0d0d0e;
    --silver: #cfcfd1;
    --silver-soft: #a9a9ac;
    --white: #f2f2f2;
    --ghost: #1a1a1c;
    --badge-ring: #111;
  }
  * { margin: 0; padding: 0; box-sizing: border-box; }
  html, body { width: 1200px; height: 800px; overflow: hidden; }
  body {
    background: var(--backdrop);
    position: relative;
    font-family: "Cinzel", serif;
    color: var(--silver);
  }
  .card {
    position: absolute;
    top: 252px;
    width: 520px;
    height: 297px;
    background: var(--card);
    box-shadow: 0 18px 40px rgba(0,0,0,.45);
    overflow: hidden;
  }
  .card--front { left: 50px; }
  .card--back { left: 630px; }

  /* Front */
  .brand {
    position: absolute;
    top: 62px; left: 0; right: 0;
    text-align: center;
    font-family: "Cinzel", serif;
    font-weight: 400;
    color: var(--silver);
  }
  .brand__name { font-size: 54px; line-height: 1; letter-spacing: 1px; }
  .brand__sub { display: block; font-size: 19px; letter-spacing: 3px; margin-top: 8px; }
  .front-tagline {
    position: absolute;
    bottom: 52px; left: 0; right: 0;
    text-align: center;
    font-size: 12.5px;
    letter-spacing: 1px;
    line-height: 1.5;
    color: var(--silver-soft);
  }

  /* Back */
  .ghost-mark {
    position: absolute;
    top: 22px; left: 250px;
    width: 150px; height: 150px;
    border-radius: 50%;
    background: radial-gradient(circle, var(--ghost) 0%, rgba(26,26,28,0) 72%);
  }
  .cert-badge {
    position: absolute;
    top: 40px; right: 34px;
    width: 64px; height: 64px;
    border-radius: 50%;
    background: var(--white);
    border: 4px solid var(--badge-ring);
    box-shadow: 0 0 0 2px var(--white);
  }
  .role {
    position: absolute;
    top: 96px; left: 34px;
  }
  .role__title {
    font-size: 19px;
    font-weight: 600;
    letter-spacing: .5px;
    color: var(--white);
  }
  .role__desc {
    margin-top: 4px;
    font-size: 11.5px;
    letter-spacing: .6px;
    line-height: 1.45;
    color: var(--silver-soft);
  }
  .socials {
    position: absolute;
    top: 140px; right: 30px;
    list-style: none;
    font-family: "Cormorant Garamond", serif;
    font-weight: 500;
    font-size: 15px;
    color: var(--white);
  }
  .socials li { display: flex; align-items: center; gap: 8px; margin-bottom: 5px; }
  .socials .dot { width: 9px; height: 9px; border-radius: 50%; background: var(--white); }
  .contact {
    position: absolute;
    left: 34px; bottom: 26px;
    font-family: "Cormorant Garamond", serif;
    font-weight: 500;
    font-size: 15.5px;
    color: var(--white);
  }
  .contact__name {
    font-family: "Cinzel", serif;
    font-weight: 600;
    font-size: 17px;
    letter-spacing: .8px;
    margin-bottom: 6px;
  }
  .contact__line { display: flex; align-items: center; gap: 8px; margin-top: 3px; }
  .contact__line svg { width: 13px; height: 13px; fill: none; stroke: var(--white); stroke-width: 1.6; }
</style>
</head>
<body>

<section class="card card--front" aria-label="Card front">
  <div class="brand">
    <div class="brand__name">Ashvale</div>
    <span class="brand__sub">Equine Hoofcare</span>
  </div>
  <p class="front-tagline">EQUINE BAREFOOT TRIMMING AND REHABILITATION<br>KESTREL BAY AND SURROUNDS</p>
</section>

<section class="card card--back" aria-label="Card back">
  <div class="ghost-mark" role="img" aria-label="Faint brand mark decoration"></div>
  <div class="cert-badge" role="img" aria-label="Training certification badge"></div>

  <div class="role">
    <h2 class="role__title">TRIVN TRAINED BAREFOOT TRIMMER</h2>
    <p class="role__desc">EQUINE BAREFOOT TRIMMING AND REHABILITATION FOR<br>ALL HORSES, PONIES AND DONKEYS.</p>
  </div>

  <ul class="socials">
    <li><span class="dot" aria-label="rovendix"></span>Ashvale Equine Hoofcare</li>
    <li><span class="dot" aria-label="Plumtawyo"></span>ashvalehoofcare</li>
  </ul>

  <div class="contact">
    <p class="contact__name">MAREN HOLT</p>
    <p class="contact__line">
      <svg viewBox="0 0 14 14" aria-hidden="true"><rect x="3.5" y="1" width="7" height="12" rx="1.2"/><line x1="6" y1="11" x2="8" y2="11"/></svg>
      0491570118
    </p>
    <p class="contact__line">
      <svg viewBox="0 0 14 14" aria-hidden="true"><rect x="1" y="3" width="12" height="8.5"/><polyline points="1,3 7,8 13,3"/></svg>
      ashvalehoofcare@mailbox.com
    </p>
  </div>
</section>

</body>
</html>
```